Business card for home developer

Name, email, phone #, logo, address, lic # and slogan.
Slogan to say something like, "Leader in quality neighborhood communities" maybe? The last one said "A sept above the rest". Some thing saying we are above the other people.
The card can be two sided?
Home buyers
Business

```html
<!DOCTYPE html>
<html lang="en">
<head>
<meta charset="utf-8">
<title>Harborline Homes – Business Cards</title>
<link href="https://fonts.googleapis.com/css2?family=Open+Sans:wght@400;700;800&display=swap" rel="stylesheet">
<style>
  :root {
    --stage: #000000;
    --paper: #ffffff;
    --brand-red: #a82422;
    --brand-blue: #284785;
    --ink: #111111;
  }
  html, body {
    margin: 0;
    padding: 0;
    width: 1200px;
    height: 900px;
    overflow: hidden;
    background: var(--stage);
    font-family: "Open Sans", Arial, sans-serif;
  }
  .canvas { position: relative; width: 1200px; height: 900px; }

  .card {
    position: absolute;
    background: var(--paper);
    overflow: hidden;
  }
  .card--front-red  { left: 3px;   top: 84px;  width: 564px; height: 328px; --accent: var(--brand-red); }
  .card--back-red   { left: 570px; top: 33px;  width: 630px; height: 368px; --accent: var(--brand-red); }
  .card--back-blue  { left: 14px;  top: 455px; width: 574px; height: 335px; --accent: var(--brand-blue); }
  .card--front-blue { left: 571px; top: 473px; width: 629px; height: 368px; --accent: var(--brand-blue); }

  .houses {
    position: absolute;
    left: 0; right: 0;
    background: linear-gradient(to bottom, var(--paper) 0%, var(--accent) 100%);
  }
  .band {
    position: absolute;
    left: 0; right: 0; bottom: 0;
    background: var(--accent);
  }

  .wordmark {
    position: absolute;
    display: flex;
    align-items: center;
    gap: 12px;
    color: var(--brand-blue);
    font-weight: 800;
    letter-spacing: -0.5px;
    white-space: nowrap;
  }
  .wordmark__dot {
    border-radius: 50%;
    background: var(--brand-red);
    flex: none;
  }

  .slogan {
    position: absolute;
    font-size: 11px;
    white-space: nowrap;
  }
  .card--back-red .slogan  { color: var(--brand-red); }
  .card--back-blue .slogan { color: var(--brand-blue); }

  .person {
    position: absolute;
    font-family: Arial, "Open Sans", sans-serif;
    color: var(--ink);
    font-size: 14px;
    line-height: 18px;
  }
  .person__name { text-transform: uppercase; }

  .web {
    position: absolute;
    left: 0; right: 0;
    text-align: center;
    color: var(--paper);
    font-size: 16px;
  }

  .icon {
    position: absolute;
    width: 12px;
    height: 12px;
  }
  .icon svg { width: 12px; height: 12px; display: block; }
</style>
</head>
<body>
<main class="canvas">

  <!-- Front, red -->
  <section class="card card--front-red">
    <div class="wordmark" style="left:110px; top:100px; font-size:40px;">
      Harborline Homes<span class="wordmark__dot" style="width:24px;height:24px;"></span>
    </div>
    <div class="houses" role="img" aria-label="Row of house silhouettes" style="top:193px; height:61px;"></div>
    <div class="band" style="height:74px;"></div>
    <p class="web" style="top:274px; margin:0;">www.yourwebpage.com</p>
  </section>

  <!-- Back, red -->
  <section class="card card--back-red">
    <div class="wordmark" style="left:22px; top:52px; font-size:28px;">
      Harborline Homes<span class="wordmark__dot" style="width:16px;height:16px;"></span>
    </div>
    <p class="slogan" style="left:28px; top:139px; margin:0;">"Leader in quality neighborhood communities"</p>
    <div class="person" style="left:392px; top:126px;">
      <div class="person__name">Your Name</div>
      <div>Your position</div>
    </div>
    <div class="houses" role="img" aria-label="Row of house silhouettes" style="top:217px; height:68px;"></div>
    <div class="band" style="height:83px;"></div>
    <span class="icon" style="left:40px; top:311px;"><svg viewBox="0 0 12 12"><path d="M3 1l2 2.5-1.2 1.2c.6 1.4 1.6 2.4 3 3L8 6.5 10.5 8.5 9.5 11C5 10.5 1.5 7 1 2.5z" fill="#fff"/></svg></span>
    <span class="icon" style="left:40px; top:335px;"><svg viewBox="0 0 12 12"><rect x="1" y="2.5" width="10" height="7" fill="none" stroke="#fff" stroke-width="1.4"/><path d="M1 2.5l5 4 5-4" fill="none" stroke="#fff" stroke-width="1.2"/></svg></span>
    <span class="icon" style="left:379px; top:311px;"><svg viewBox="0 0 12 12"><circle cx="6" cy="6" r="5" fill="none" stroke="#fff" stroke-width="1.3"/><path d="M1 6h10M6 1c-2.5 3-2.5 7 0 10M6 1c2.5 3 2.5 7 0 10" fill="none" stroke="#fff" stroke-width="1"/></svg></span>
    <span class="icon" style="left:379px; top:335px;"><svg viewBox="0 0 12 12"><path d="M6 11.5S2 7 2 4.5a4 4 0 0 1 8 0C10 7 6 11.5 6 11.5z" fill="none" stroke="#fff" stroke-width="1.4"/><circle cx="6" cy="4.5" r="1.3" fill="#fff"/></svg></span>
  </section>

  <!-- Back, blue -->
  <section class="card card--back-blue">
    <div class="wordmark" style="left:18px; top:42px; font-size:26px;">
      Harborline Homes<span class="wordmark__dot" style="width:15px;height:15px;"></span>
    </div>
    <p class="slogan" style="left:24px; top:127px; margin:0;">"Leader in quality neighborhood communities"</p>
    <div class="person" style="left:357px; top:116px;">
      <div class="person__name">Your Name</div>
      <div>Your position</div>
    </div>
    <div class="houses" role="img" aria-label="Row of house silhouettes" style="top:198px; height:62px;"></div>
    <div class="band" style="height:75px;"></div>
    <span class="icon" style="left:36px; top:284px;"><svg viewBox="0 0 12 12"><path d="M3 1l2 2.5-1.2 1.2c.6 1.4 1.6 2.4 3 3L8 6.5 10.5 8.5 9.5 11C5 10.5 1.5 7 1 2.5z" fill="#fff"/></svg></span>
    <span class="icon" style="left:36px; top:306px;"><svg viewBox="0 0 12 12"><rect x="1" y="2.5" width="10" height="7" fill="none" stroke="#fff" stroke-width="1.4"/><path d="M1 2.5l5 4 5-4" fill="none" stroke="#fff" stroke-width="1.2"/></svg></span>
    <span class="icon" style="left:345px; top:284px;"><svg viewBox="0 0 12 12"><circle cx="6" cy="6" r="5" fill="none" stroke="#fff" stroke-width="1.3"/><path d="M1 6h10M6 1c-2.5 3-2.5 7 0 10M6 1c2.5 3 2.5 7 0 10" fill="none" stroke="#fff" stroke-width="1"/></svg></span>
    <span class="icon" style="left:345px; top:306px;"><svg viewBox="0 0 12 12"><path d="M6 11.5S2 7 2 4.5a4 4 0 0 1 8 0C10 7 6 11.5 6 11.5z" fill="none" stroke="#fff" stroke-width="1.4"/><circle cx="6" cy="4.5" r="1.3" fill="#fff"/></svg></span>
  </section>

  <!-- Front, blue -->
  <section class="card card--front-blue">
    <div class="wordmark" style="left:112px; top:104px; font-size:46px;">
      Harborline Homes<span class="wordmark__dot" style="width:26px;height:26px;"></span>
    </div>
    <div class="houses" role="img" aria-label="Row of house silhouettes" style="top:217px; height:70px;"></div>
    <div class="band" style="height:81px;"></div>
    <p class="web" style="top:308px; margin:0; font-size:18px;">www.yourwebpage.com</p>
  </section>

</main>
</body>
</html>
```